Professional business cards for real estate development company

I need business cards for my new real estate development company. The company, "KORVA" is a real estate development, investment, and advisory firm with a focus on multifamily, office, and mixed-use projects across primary and secondary markets in the Southeast United States.

Style preference is modern

Industry/Entity Type

Real Estate Development

Contact Information for Business Card

The business cards need to include:
Name
Title
Mailing Address
Phone Number
Web Address

Logo is attached. I would like white to be the primary color with incorporation of the company colors: #232D3A and #B5A451

Font styles to use
Other font styles liked:
• Montserrat, Avenir

Requirements
Must have
• Company Logo. No need to include the company name since the name is in the logo.
Should not have
• No line type designs

```html
<!DOCTYPE html>
<html lang="en">
<head>
<meta charset="UTF-8">
<title>KORVA Business Card</title>
<link href="https://fonts.googleapis.com/css2?family=Montserrat:wght@400;500;600;700&display=swap" rel="stylesheet">
<style>
  :root {
    --navy: #232D3A;
    --gold: #B5A451;
    --white: #FFFFFF;
    --card-white: #F8F8F7;
    --backdrop: #E4E4E2;
  }
  * { margin: 0; padding: 0; box-sizing: border-box; }
  html, body { width: 1200px; height: 675px; overflow: hidden; }
  body {
    background: var(--backdrop);
    font-family: "Montserrat", sans-serif;
    color: var(--navy);
  }
  .canvas {
    width: 1200px; height: 675px;
    display: flex; align-items: center; justify-content: center;
    gap: 60px;
  }
  .card {
    width: 490px; height: 280px;
    border-radius: 16px;
    position: relative;
    box-shadow: 0 10px 28px rgba(35, 45, 58, 0.18);
    overflow: hidden;
  }
  .card-front { background: var(--card-white); }
  .card-back {
    background: var(--navy);
    display: flex; align-items: center; justify-content: center;
  }
  .brand-name {
    font-weight: 600;
    letter-spacing: 3px;
    line-height: 1;
  }
  .card-front .brand-name {
    position: absolute; left: 34px; top: 42px;
    font-size: 40px; color: var(--navy);
  }
  .card-back .brand-name {
    font-size: 52px; color: var(--white);
  }
  .person {
    position: absolute; right: 44px; top: 70px;
    text-align: left;
  }
  .person-name {
    font-weight: 600; font-size: 22px; color: var(--gold);
    letter-spacing: 1px; line-height: 1.1;
  }
  .person-title {
    font-weight: 600; font-size: 12px; color: var(--navy);
  }
  .contact-list {
    position: absolute; left: 262px; top: 146px;
    list-style: none;
    font-size: 13px; font-weight: 500; color: var(--navy);
  }
  .contact-item {
    display: flex; align-items: flex-start; gap: 10px;
    line-height: 1.35; margin-bottom: 3px;
  }
  .contact-icon {
    width: 14px; height: 14px; flex: none; margin-top: 2px;
    fill: var(--gold);
  }
</style>
</head>
<body>
<main class="canvas">
  <section class="card card-front">
    <div class="brand-name">KORVA</div>

    <div class="person">
      <div class="person-name">NAME</div>
      <div class="person-title">Designation</div>
    </div>

    <ul class="contact-list">
      <li class="contact-item">
        <svg class="contact-icon" viewBox="0 0 14 14"><path d="M7 0a5 5 0 0 0-5 5c0 3.6 5 9 5 9s5-5.4 5-9a5 5 0 0 0-5-5zm0 7a2 2 0 1 1 0-4 2 2 0 0 1 0 4z"/></svg>
        <span>Steet Name,<br>Zip Code &amp; Town</span>
      </li>
      <li class="contact-item">
        <svg class="contact-icon" viewBox="0 0 14 14"><path d="M3 1l2.5 0 1 3-1.5 1a8 8 0 0 0 4 4l1-1.5 3 1V11a2 2 0 0 1-2 2C5.5 13 1 8.5 1 3a2 2 0 0 1 2-2z"/></svg>
        <span>Phone No.</span>
      </li>
      <li class="contact-item">
        <svg class="contact-icon" viewBox="0 0 14 14"><path d="M1 3h12v8H1z M1 3l6 4.5L13 3" stroke="#F8F8F7" stroke-width="1"/></svg>
        <span>Email ID</span>
      </li>
      <li class="contact-item">
        <svg class="contact-icon" viewBox="0 0 14 14"><circle cx="7" cy="7" r="6"/><path d="M1 7h12M7 1c-2.5 3-2.5 9 0 12M7 1c2.5 3 2.5 9 0 12" stroke="#F8F8F7" stroke-width="0.9" fill="none"/></svg>
        <span>Web Address</span>
      </li>
    </ul>
  </section>

  <section class="card card-back">
    <div class="brand-name">KORVA</div>
  </section>
</main>
</body>
</html>
```